Business Card Design Quokka Celebration Co

on the front i would like to see the logo and my contact details. on the back i would like it to include the 3 parts to the business party planning, party hire and party supplies also with a line at the bottom (or white space) to write their appointment details.

Target Market(s)

mums and corporates

Industry/Entity Type

Business

Requirements
Must have
• logo and contact details which are: Name: Janelle, Phone: 0417263954, email: jan@quokkaevents.com.au, Website: www.quokkaevents.com.au,

```html
<!DOCTYPE html>
<html lang="en">
<head>
<meta charset="utf-8">
<title>Quokka Celebration Co – Business Card</title>
<link rel="stylesheet" href="https://fonts.googleapis.com/css2?family=Lato:wght@300;400;700;900&family=Courgette&display=swap">
<style>
  :root {
    --backdrop: #ece8e3;
    --card-white: #ffffff;
    --purple-deep: #4f3aa2;
    --purple-light: #7d70c4;
    --cyan: #2fb9e0;
    --cyan-light: #4fcdf0;
    --yellow: #f6b81f;
    --script-yellow: #f7c625;
    --magenta: #b44fae;
    --blue: #27a3dc;
    --text-grey: #3d3d3d;
    --rule-grey: #c9c9c9;
    --link-grey: #6b6b8a;
  }
  * { box-sizing: border-box; margin: 0; padding: 0; }
  html, body { width: 1200px; height: 840px; overflow: hidden; }
  body {
    background: var(--backdrop);
    font-family: "Lato", Arial, sans-serif;
    position: relative;
  }
  .card {
    position: absolute;
    border-radius: 4px;
    box-shadow: 0 10px 28px rgba(0,0,0,0.18);
    overflow: hidden;
  }

  /* Front */
  .card-front {
    left: 110px; top: 122px;
    width: 340px; height: 596px;
    background: var(--card-white);
  }
  .brand {
    position: absolute; left: 0; top: 56px; width: 100%;
    text-align: center;
  }
  .brand-dot {
    width: 66px; height: 66px; border-radius: 50%;
    background: var(--purple-light);
    margin: 0 auto 18px;
  }
  .brand-name {
    font-weight: 900; font-size: 34px; line-height: 1.1;
    color: var(--cyan);
    letter-spacing: 0.5px;
  }
  .name-tab {
    position: absolute; left: 0; top: 262px;
    width: 196px; height: 56px;
    background: linear-gradient(180deg, var(--cyan-light), var(--cyan));
    border-radius: 0 6px 6px 0;
    color: #fff;
    font-weight: 700; font-size: 27px; letter-spacing: 1px;
    display: flex; align-items: center; justify-content: center;
  }
  .contact-list { position: absolute; left: 0; top: 350px; width: 100%; list-style: none; }
  .contact-item {
    position: relative; height: 68px;
    display: flex; align-items: center;
  }
  .contact-item::after {
    content: ""; position: absolute; left: 58px; right: 20px; bottom: 0;
    height: 1px; background: var(--rule-grey);
  }
  .contact-item:last-child::after { display: none; }
  .contact-icon {
    width: 42px; height: 38px; border-radius: 0 5px 5px 0;
    display: flex; align-items: center; justify-content: center;
    margin-right: 22px;
  }
  .contact-icon svg { width: 20px; height: 20px; fill: #fff; }
  .icon-phone { background: var(--yellow); }
  .icon-mail { background: var(--magenta); }
  .icon-web { background: var(--blue); }
  .contact-text { font-size: 16px; color: var(--text-grey); }
  .front-band {
    position: absolute; left: 0; bottom: 0; width: 100%; height: 28px;
    background: var(--purple-deep);
  }

  /* Back */
  .card-back {
    left: 520px; top: 250px;
    width: 596px; height: 340px;
    background: linear-gradient(110deg, var(--purple-deep) 0%, var(--purple-light) 100%);
  }
  .services {
    position: absolute; left: 34px; top: 26px;
    font-family: "Courgette", cursive;
    font-size: 27px; line-height: 1.35;
    color: var(--script-yellow);
  }
  .appointment-box {
    position: absolute; left: 34px; top: 128px;
    width: 528px; height: 176px;
  }
  .appointment-box svg.box-shape { position: absolute; inset: -22px 0 0 0; width: 528px; height: 198px; }
  .appointment-label {
    position: absolute; left: 34px; top: 18px;
    font-weight: 300; font-size: 19px;
    color: var(--link-grey);
    text-decoration: underline;
    text-underline-offset: 3px;
  }
</style>
</head>
<body>

<section class="card card-front" aria-label="Business card front">
  <div class="brand">
    <div class="brand-dot"></div>
    <p class="brand-name">Quokka<br>Celebration Co</p>
  </div>

  <div class="name-tab">JANELLE</div>

  <ul class="contact-list">
    <li class="contact-item">
      <span class="contact-icon icon-phone">
        <svg viewBox="0 0 24 24" aria-hidden="true"><path d="M6.6 10.8a15.1 15.1 0 0 0 6.6 6.6l2.2-2.2c.3-.3.7-.4 1-.2 1.1.4 2.3.6 3.6.6.6 0 1 .4 1 1V20c0 .6-.4 1-1 1A17 17 0 0 1 3 4c0-.6.4-1 1-1h3.5c.6 0 1 .4 1 1 0 1.3.2 2.5.6 3.6.1.3 0 .7-.2 1l-2.3 2.2z"/></svg>
      </span>
      <span class="contact-text">0417263954</span>
    </li>
    <li class="contact-item">
      <span class="contact-icon icon-mail">
        <svg viewBox="0 0 24 24" aria-hidden="true"><path d="M3 6h18v12H3z" opacity="0"/><path d="M3 6.5V18h18V6.5l-9 6-9-6zM3.6 6l8.4 5.6L20.4 6z"/></svg>
      </span>
      <span class="contact-text">jan@quokkaevents.com.au</span>
    </li>
    <li class="contact-item">
      <span class="contact-icon icon-web">
        <svg viewBox="0 0 24 24" aria-hidden="true"><path d="M12 2a7 7 0 0 0-7 7c0 5.2 7 13 7 13s7-7.8 7-13a7 7 0 0 0-7-7zm0 9.5a2.5 2.5 0 1 1 0-5 2.5 2.5 0 0 1 0 5z"/></svg>
      </span>
      <span class="contact-text">www.quokkaevents.com.au</span>
    </li>
  </ul>

  <div class="front-band"></div>
</section>

<section class="card card-back" aria-label="Business card back">
  <p class="services">Party planning,<br>Party hire and Party supplies</p>
  <div class="appointment-box">
    <svg class="box-shape" viewBox="0 0 528 198" aria-hidden="true">
      <path d="M0 22 H30 L48 0 L66 22 H516 Q528 22 528 34 V186 Q528 198 516 198 H12 Q0 198 0 186 Z" fill="#ffffff"/>
    </svg>
    <span class="appointment-label">make an appointment</span>
  </div>
</section>

</body>
</html>
```